Need 8.5" x 11" as well as large 11"x17" Posters for our upcoming event

Please include LOGOs in poster
Main logo is Harborview Teen Circle of PL

All high school age faith groups are invited to come and join with 150 to 175 other high school students from various faith traditions to participate in the Harborview Teen Circle of Pine Lakes‘s Annual Kindred Voices Gathering. More than ever, our county and world need young leaders who are willing to learn from each other and build stronger communities!

KINDRED GATHERING
The purpose of this Interfaith Youth Forum is to bring together young people from diverse ethnic, cultural, and religious backgrounds, and to engage them in dialogue. True dialogue is a conversation on a common subject between two or more persons of differing points of view and/or backgrounds. We feel that this commitment to dialogue will affect relationships in a constructive way in our places of worship and in our community.
The forum itself involves having eight religiously diverse high school-age students, one adult, and youth leader around each table to discuss common questions. Our youth leaders act as facilitators, but it is stressed that it is the students we want to hear from.
RSVP for our KINDRED GATHERING before February 18th, 2018
FORUM QUESTIONS Available online at http://htcpl-example.org/home/kindred-fair/

Target Market(s)

Houses of worship, community leaders, High School Students

Industry/Entity Type

Non-Profit

Font styles to use
Serif

Colors
cfdeed
0255a3
f78f20
f37122
f68d4d
faa54b
ffcf3e
ffc214
34a6d7

Requirements
Must have
• Harborview Teen Circle of Pine Lakes's 14th Annual Kindred Gathering & Fair
• TEENS EXPRESSING THEIR FAITH THROUGH ART, MUSIC, AND DIALOGUE
• THIS YEAR'S THEME: “Who Are You?”
• Sunday, March 11th, 2018 11:00am-5:00pm
• Congregation Ner Adamah
• 4187 W Larkmont Rd. Santa Ana, CA 92705
• Email: htcplorg@mailbox-example.com
• Website: HTCPL-example.org
• Facebook: Harborview Teen Circle of Pine Lakes
Nice to have
• Descriptions provided in word doc
Should not have
• -

```html
<!DOCTYPE html>
<html lang="en">
<head>
<meta charset="utf-8">
<title>Harborview Teen Circle of Pine Lakes – Kindred Gathering &amp; Fair Flyer</title>
<link rel="stylesheet" href="https://fonts.googleapis.com/css2?family=Ubuntu:wght@400;500;700&family=Open+Sans:wght@400;600;700&display=swap">
<style>
:root{
  --blue:#0255a3;
  --blue-deep:#0a4d9a;
  --orange:#f37122;
  --orange-light:#f78f20;
  --amber:#faa54b;
  --ink:#333;
  --paper:#f4f4f2;
  --backdrop:#e8e4dc;
}
*{margin:0;padding:0;box-sizing:border-box}
html,body{width:1200px;height:789px;overflow:hidden;background:var(--backdrop)}
.canvas{position:relative;width:1200px;height:789px}
.page{position:absolute;top:78px;width:490px;height:633px;background:var(--paper);overflow:hidden;font-family:"Open Sans",sans-serif;color:var(--ink)}
.page--front{left:95px}
.page--back{left:616px}
.hero{position:absolute;left:0;top:0;width:490px;height:360px}
.badge{position:absolute;top:12px;right:12px;width:74px;height:74px;border-radius:50%;background:#fff;border:3px solid #d6d6d6;display:flex;align-items:center;justify-content:center;text-align:center;font-family:"Ubuntu",sans-serif;font-size:7px;line-height:1.2;color:#555;padding:8px}
.title{position:absolute;left:0;width:490px;text-align:center;top:310px;font-family:"Ubuntu",sans-serif}
.title__org{color:var(--orange);font-size:16px}
.title__event{color:var(--blue);font-size:17.5px;font-weight:700;margin-top:1px}
.tagline{position:absolute;left:97px;width:420px;top:354px;border-top:1px solid #999;border-bottom:1px solid #999;font-family:"Ubuntu",sans-serif;font-size:11px;color:#555;text-align:center;padding:3px 0;width:325px}
.theme{position:absolute;left:131px;top:387px;width:224px;height:30px}
.theme__text{position:absolute;inset:0;display:flex;align-items:center;justify-content:center;font-family:"Ubuntu",sans-serif;font-weight:700;font-size:21px;color:#fff}
.details{position:absolute;left:135px;top:438px;width:220px;height:62px;border:1px solid var(--blue);text-align:center;font-family:"Ubuntu",sans-serif;font-size:11px;line-height:14.5px;padding-top:2px;background:var(--paper)}
.details__date{position:absolute;top:-8px;left:0;width:100%;color:var(--orange)}
.details__date span{background:var(--paper);padding:0 5px}
.details__date b{color:var(--blue);font-weight:500}
.details__time{color:var(--blue);font-weight:500;margin-top:10px}
.details__venue{color:var(--orange);font-weight:700}
.details__address{color:var(--blue)}
.intro{position:absolute;left:35px;top:517px;width:440px;font-size:7px;line-height:10.5px;color:#333}
.partners{position:absolute;display:flex;align-items:center;gap:60px}
.partners--front{left:40px;top:564px}
.partners--back{left:280px;top:570px;gap:42px}
.partner{display:flex;align-items:center;gap:5px;font-family:"Ubuntu",sans-serif;font-size:11px;color:var(--blue)}
.partner__mark{width:16px;height:16px;border-radius:50%;border:1.5px solid var(--blue)}
.footer{position:absolute;left:0;bottom:0;width:490px;height:48px}
.footer__links{position:absolute;bottom:7px;display:flex;gap:8px;font-size:7px;color:#fff;align-items:center;white-space:nowrap}
.footer__links .sep{opacity:.7}
.footer__links .dot{display:inline-block;width:8px;height:8px;border:1px solid #fff;border-radius:50%;margin-right:3px;vertical-align:-1px}
.footer__phone{position:absolute;top:2px;display:flex;align-items:center;gap:8px;font-family:"Ubuntu",sans-serif;font-size:16px;color:#fff}
.section-tab{position:absolute;left:196px;width:112px;height:19px}
.section-tab__text{position:absolute;inset:0;display:flex;align-items:center;justify-content:center;font-family:"Ubuntu",sans-serif;font-size:10px;font-weight:500;color:#fff;letter-spacing:.2px}
.copy{position:absolute;left:21px;width:460px;font-size:7px;line-height:10.4px;color:#333}
.copy .accent{color:var(--orange)}
.copy .strong{color:var(--blue);font-weight:700}
</style>
</head>
<body>
<div class="canvas">

  <!-- Front page -->
  <section class="page page--front">
    <svg class="hero" viewBox="0 0 490 360" aria-hidden="false">
      <defs>
        <linearGradient id="frontPhoto" x1="0" y1="0" x2="0" y2="1">
          <stop offset="0" stop-color="#8a1e22"/>
          <stop offset=".45" stop-color="#5a6a8c"/>
          <stop offset="1" stop-color="#6b5a48"/>
        </linearGradient>
        <linearGradient id="frontBand" x1="0" y1="0" x2="1" y2="0">
          <stop offset="0" stop-color="#fbd3b2"/>
          <stop offset=".6" stop-color="#f78f20"/>
          <stop offset="1" stop-color="#f37122"/>
        </linearGradient>
      </defs>
      <rect role="img" aria-label="Group photo of teens from many faith communities on a stage" x="0" y="0" width="490" height="320" fill="url(#frontPhoto)"/>
      <polygon points="0,318 313,220 490,296 490,324 313,232 0,330" fill="url(#frontBand)"/>
      <polygon points="313,232 490,324 490,342 313,240" fill="var(--blue)"/>
      <polygon points="0,330 313,240 490,342 490,360 0,360" fill="var(--paper)"/>
    </svg>
    <div class="badge">Harborview Teen Circle of Pine Lakes</div>

    <div class="title">
      <div class="title__org">Harborview Teen Circle of Pine Lakes's</div>
      <div class="title__event">14th Annual Kindred Gathering &amp; Fair</div>
    </div>
    <div class="tagline">Teens Expressing Their Faith Through Art, Music, And Dialogue</div>

    <div class="theme">
      <svg width="224" height="30" viewBox="0 0 224 30">
        <polygon points="0,2 224,2 214,15 224,28 0,28 10,15" fill="var(--orange)"/>
      </svg>
      <div class="theme__text">Who Are You?</div>
    </div>

    <div class="details">
      <div class="details__date"><span>Sunday,11<sup style="font-size:6px">th</sup> March , <b>2018</b></span></div>
      <div class="details__time">11:00am - 5:00pm</div>
      <div class="details__venue">Congregation Ner Adamah</div>
      <div class="details__address">4187 W Larkmont Rd. Santa Ana, <b>CA 92705</b></div>
    </div>

    <p class="intro">All high school age faith groups are invited to come and join with 150 to 175 other high school students from various faith traditions to participate in the Harborview Teen Circle of Pine Lakes's Annual Kindred Voices Gathering. More than ever, our county and world need young leaders who are willing to learn from each other and build stronger communities!</p>

    <div class="partners partners--front">
      <div class="partner"><span>Clearpath Allies</span><span class="partner__mark"></span></div>
      <div class="partner"><span class="partner__mark"></span><span>Congregation Ner Adamah</span></div>
    </div>

    <div class="footer">
      <svg width="490" height="48" viewBox="0 0 490 48">
        <polygon points="0,19 318,19 330,0 490,0 490,48 0,48" fill="var(--blue)"/>
        <polyline points="0,18 317,18 329,-1 490,-1" fill="none" stroke="var(--orange)" stroke-width="2"/>
      </svg>
      <div class="footer__phone" style="left:340px">
        <svg width="16" height="16" viewBox="0 0 24 24"><path d="M6.6 10.8a15 15 0 0 0 6.6 6.6l2.2-2.2a1 1 0 0 1 1-.25 11.4 11.4 0 0 0 3.6.57 1 1 0 0 1 1 1V20a1 1 0 0 1-1 1A17 17 0 0 1 3 4a1 1 0 0 1 1-1h3.5a1 1 0 0 1 1 1c0 1.25.2 2.45.57 3.57a1 1 0 0 1-.25 1z" fill="var(--orange-light)"/></svg>
        <span>(555) 014-2290</span>
      </div>
      <div class="footer__links" style="left:12px">
        <span><i class="dot"></i>htcpl-example.org</span><span class="sep">|</span>
        <span><i class="dot"></i>htcplorg@mailbox-example.com</span><span class="sep">|</span>
        <span><i class="dot"></i>Harborview Teen Circle of Pine Lakes</span>
      </div>
    </div>
  </section>

  <!-- Back page -->
  <section class="page page--back">
    <svg class="hero" viewBox="0 0 490 360">
      <defs>
        <linearGradient id="backPhoto" x1="0" y1="0" x2="0" y2="1">
          <stop offset="0" stop-color="#1e1a18"/>
          <stop offset=".5" stop-color="#5a3c3a"/>
          <stop offset="1" stop-color="#b0804e"/>
        </linearGradient>
        <linearGradient id="backBand" x1="0" y1="0" x2="1" y2="0">
          <stop offset="0" stop-color="#f37122"/>
          <stop offset=".35" stop-color="#f78f20"/>
          <stop offset="1" stop-color="#fbd3b2"/>
        </linearGradient>
      </defs>
      <rect role="img" aria-label="Photo of teen dancers performing on a stage" x="0" y="0" width="490" height="320" fill="url(#backPhoto)"/>
      <polygon points="0,290 176,222 490,318 490,330 176,234 0,318" fill="url(#backBand)"/>
      <polygon points="0,318 176,234 176,242 0,330" fill="var(--blue)"/>
      <polygon points="0,330 176,242 490,330 490,360 0,360" fill="var(--paper)"/>
    </svg>
    <div class="badge">Harborview Teen Circle of Pine Lakes</div>

    <div class="section-tab" style="top:310px">
      <svg width="112" height="19" viewBox="0 0 112 19"><polygon points="8,0 112,0 104,19 0,19" fill="var(--blue)"/><polygon points="12,0 108,0 100,19 4,19" fill="var(--orange)"/></svg>
      <div class="section-tab__text">KINDRED GATHERING</div>
    </div>
    <div class="copy" style="top:335px">
      The purpose of this Interfaith Youth Forum is to bring together young people from diverse ethnic, cultural, and religious backgrounds, and to engage them in dialogue. True dialogue is a conversation on a common subject between two or more persons of differing points of view and/or backgrounds. We feel that this commitment to dialogue will affect relationships in a constructive way in our places of worship and in our community.<br>
      The forum itself involves having eight religiously diverse high school-age students, one adult, and youth leader around each table to discuss common questions. Our youth leaders act as facilitators, but it is stressed that it is the students we want to hear from.
    </div>
    <div class="copy" style="top:403px">
      <span class="accent">RSVP for our KINDRED GATHERING before</span> <span class="strong">February 18th, 2018</span><br>
      <span class="strong">FORUM QUESTIONS Available online at</span> <span class="accent">http://htcpl-example.org/home/kindred-fair/</span>
    </div>

    <div class="section-tab" style="top:433px">
      <svg width="112" height="19" viewBox="0 0 112 19"><polygon points="8,0 112,0 104,19 0,19" fill="var(--blue)"/><polygon points="12,0 108,0 100,19 4,19" fill="var(--orange)"/></svg>
      <div class="section-tab__text">FAITH FESTIVAL</div>
    </div>
    <div class="copy" style="top:458px">
      The forum will include our Faith Festival portion of the program which families of the participants are welcomed to join. The Festival will include musical performances of all types from diverse religious communities. The differing performing arts include but are not limited to singing, dancing, instrumental music, storytelling, etc.<br>
      To Participate in our Faith Festival <span class="strong">(Music, Song, Dance), RSVP by February 11th, 2018</span>
    </div>

    <div class="section-tab" style="top:506px">
      <svg width="112" height="19" viewBox="0 0 112 19"><polygon points="8,0 112,0 104,19 0,19" fill="var(--blue)"/><polygon points="12,0 108,0 100,19 4,19" fill="var(--orange)"/></svg>
      <div class="section-tab__text">ART GALLERY</div>
    </div>
    <div class="copy" style="top:532px">
      This event will include and Art Gallery display of students' work, highlighting their expressions of faith, and artwork promoting learning, understanding, leadership, and service. Art includes any painting, illustration, sculpture, photography or other visual art.<br>
      Art Work for our Art Galley must be submitted by: March 3rd, 2018
    </div>

    <div class="partners partners--back">
      <div class="partner"><span>Clearpath Allies</span><span class="partner__mark"></span></div>
      <div class="partner"><span class="partner__mark"></span><span>Congregation Ner Adamah</span></div>
    </div>

    <div class="footer">
      <svg width="490" height="48" viewBox="0 0 490 48">
        <polygon points="0,0 160,0 172,19 490,19 490,48 0,48" fill="var(--blue)"/>
        <polyline points="0,-1 161,-1 173,18 490,18" fill="none" stroke="var(--orange)" stroke-width="2"/>
      </svg>
      <div class="footer__phone" style="left:14px">
        <svg width="16" height="16" viewBox="0 0 24 24"><path d="M6.6 10.8a15 15 0 0 0 6.6 6.6l2.2-2.2a1 1 0 0 1 1-.25 11.4 11.4 0 0 0 3.6.57 1 1 0 0 1 1 1V20a1 1 0 0 1-1 1A17 17 0 0 1 3 4a1 1 0 0 1 1-1h3.5a1 1 0 0 1 1 1c0 1.25.2 2.45.57 3.57a1 1 0 0 1-.25 1z" fill="var(--orange-light)"/></svg>
        <span>(555) 014-2290</span>
      </div>
      <div class="footer__links" style="right:10px">
        <span><i class="dot"></i>htcpl-example.org</span><span class="sep">|</span>
        <span><i class="dot"></i>htcplorg@mailbox-example.com</span><span class="sep">|</span>
        <span><i class="dot"></i>Harborview Teen Circle of Pine Lakes</span>
      </div>
    </div>
  </section>

</div>
</body>
</html>
```